SkyvoraQ Business Cards and Stationary Design

Need a design for our business cards and stationary. I want to carry on the theme of the logo. I want the business cards to have a design on the back. I would like the business cards and the stationary to carry the same theme, design scheme, and branding

Target Market(s)

Airlines and Maintenance Facilities

Industry/Entity Type

Aviation

Contact Information for Business Card

Name
Position Title
Address: 4827 Tollbeck Lane, Fort Pierce, Florida, 34951
Office Number
Mobile Number
Email
Website

Font styles to use
Serif
Sans Serif

Colors

Designer to choose colors to be used in the design.

```html
<!DOCTYPE html>
<html lang="en">
<head>
<meta charset="utf-8">
<title>SkyvoraQ Business Card</title>
<link rel="stylesheet" href="https://fonts.googleapis.com/css2?family=Exo+2:wght@400;600;700;800&display=swap">
<style>
  :root {
    --backdrop: #2b2b2e;
    --card: #1d1e21;
    --card-edge: #26272b;
    --emboss: #34363b;
    --emboss-light: #44464c;
    --white: #f2f4f7;
    --muted: #b9c0c8;
    --blue: #2b9be6;
    --blue-deep: #0f5fa8;
  }
  * { box-sizing: border-box; margin: 0; padding: 0; }
  html, body { width: 800px; height: 1200px; overflow: hidden; }
  body {
    background: var(--backdrop);
    font-family: "Exo 2", sans-serif;
    position: relative;
  }
  .card {
    position: absolute;
    left: 90px;
    width: 620px;
    height: 360px;
    border-radius: 26px;
    background: var(--card);
    border: 1px solid var(--card-edge);
    overflow: hidden;
  }
  .card--front { top: 150px; }
  .card--back { top: 670px; }

  /* Front */
  .front-mark {
    position: absolute;
    left: 0; right: 0; top: 96px;
    display: flex; flex-direction: column; align-items: center;
  }
  .front-mark__dot {
    width: 74px; height: 74px; border-radius: 50%;
    background: var(--emboss);
    margin-bottom: 14px;
  }
  .front-mark__name {
    font-weight: 800;
    font-size: 50px;
    letter-spacing: 7px;
    text-transform: uppercase;
    color: var(--emboss-light);
  }

  /* Back */
  .back-name {
    position: absolute; left: 40px; top: 36px;
    font-weight: 800; font-size: 34px; letter-spacing: 5px;
    text-transform: uppercase; color: var(--white);
  }
  .person { position: absolute; left: 40px; top: 108px; }
  .person__name { font-weight: 600; font-size: 24px; color: var(--blue); }
  .person__title { font-size: 13px; color: var(--muted); margin-top: 2px; }
  .contacts { position: absolute; left: 40px; top: 176px; list-style: none; }
  .contacts li {
    display: flex; align-items: center; gap: 10px;
    font-size: 12.5px; color: var(--white); line-height: 22px;
  }
  .contacts svg { width: 12px; height: 12px; flex: none; }
  .address {
    position: absolute; left: 40px; top: 300px;
    font-size: 12.5px; color: var(--white);
  }
  .back-accent {
    position: absolute; right: -50px; top: 110px;
    width: 290px; height: 290px; border-radius: 50%;
    background: radial-gradient(circle at 35% 30%, var(--blue), var(--blue-deep));
  }
</style>
</head>
<body>
  <section class="card card--front">
    <div class="front-mark">
      <div class="front-mark__dot"></div>
      <div class="front-mark__name">SkyvoraQ</div>
    </div>
  </section>

  <section class="card card--back">
    <div class="back-name">SkyvoraQ</div>
    <div class="person">
      <div class="person__name">Marcus Delwen</div>
      <div class="person__title">Managing Director</div>
    </div>
    <ul class="contacts">
      <li><svg viewBox="0 0 12 12"><circle cx="6" cy="6" r="6" fill="var(--blue)"/></svg>(555) 014 2036</li>
      <li><svg viewBox="0 0 12 12"><circle cx="6" cy="6" r="6" fill="var(--blue)"/></svg>(555) 019 6147</li>
      <li><svg viewBox="0 0 12 12"><circle cx="6" cy="6" r="6" fill="var(--blue)"/></svg>marcus@skyvoraq.com</li>
      <li><svg viewBox="0 0 12 12"><circle cx="6" cy="6" r="6" fill="var(--blue)"/></svg>www.skyvoraq.com</li>
    </ul>
    <div class="address">4827 Tollbeck Lane, Fort Pierce, Florida, 34951</div>
    <div class="back-accent" role="img" aria-label="Large blue brand symbol decoration"></div>
  </section>
</body>
</html>
```